Profesional personal website needs design and business card

I need a business card with my professional name as a logo "Orlan Vitality" for my business. I am a Wellness Coach, consultant and trainer. So it should be professional, wellness oriented and modern.

Target Market(s)

Private clients, governments, corporations. Luxury and high market.

Industry/Entity Type

Health And Wellness

Contact Information for Business Card

Orlan Vitality should be the logo

Colors

Designer to choose colors to be used in the design.

Requirements
Must have
• Orlan Vitality
• Name: Dario Montalbe
• Wellness Coach, Consultant & Trainer.
• Website: www.orlanvitality-example.com
• Phone:
• Spain (+34) 612 480 597
• (USA) +1 (555) 318 0264
Nice to have
• The most important is the design of "Orlan Vitality", as this is going to be my personal brand logo. It should be professional, wellness, high end and actual.
Should not have
• no golds, no baroque style..

```html
<!DOCTYPE html>
<html lang="en">
<head>
<meta charset="UTF-8">
<title>Orlan Vitality – Business Card</title>
<link rel="stylesheet" href="https://fonts.googleapis.com/css2?family=Poiret+One&display=swap">
<style>
  :root {
    --bg-top: #f4f4f6;
    --bg-bottom: #b5dde5;
    --card: #1b3c4e;
    --accent: #1ba9c4;
    --ink: #ffffff;
    --icon-ink: #1b3c4e;
  }
  * { margin: 0; padding: 0; box-sizing: border-box; }
  html, body { width: 1200px; height: 1200px; overflow: hidden; }
  body {
    background: linear-gradient(180deg, var(--bg-top) 0%, var(--bg-bottom) 100%);
    font-family: "Poiret One", "Century Gothic", sans-serif;
    color: var(--ink);
    position: relative;
  }
  .card {
    position: absolute;
    left: 193px;
    width: 821px;
    height: 470px;
    background: var(--card);
    box-shadow: 0 6px 18px rgba(27, 60, 78, 0.18);
    overflow: hidden;
  }
  .card--front { top: 94px; }
  .card--back { top: 644px; }

  .pattern-area {
    position: absolute;
    display: block;
  }
  .pattern-area--front-top { right: 0; top: 0; width: 280px; height: 290px; }
  .pattern-area--front-bottom { left: 0; bottom: 0; width: 280px; height: 290px; }
  .pattern-area--back-bottom { right: 0; bottom: 0; width: 280px; height: 290px; }

  .brand-name {
    position: absolute;
    font-size: 86px;
    font-weight: 400;
    letter-spacing: 1px;
    line-height: 1;
    white-space: nowrap;
    color: var(--ink);
  }
  .card--front .brand-name {
    left: 0; right: 0;
    top: 198px;
    text-align: center;
  }
  .card--back .brand-name {
    left: 27px;
    top: 86px;
  }

  .person {
    position: absolute;
    left: 28px;
    top: 184px;
    font-size: 27px;
    line-height: 30px;
  }
  .contacts {
    position: absolute;
    left: 28px;
    top: 257px;
    list-style: none;
  }
  .contact {
    display: flex;
    align-items: center;
    height: 32px;
    margin-bottom: 12px;
    font-size: 27px;
  }
  .contact:nth-child(3) { margin-top: 1px; }
  .contact-icon {
    width: 32px; height: 32px;
    flex: none;
    margin-right: 34px;
  }
  .contact-text { white-space: nowrap; }
</style>
</head>
<body>

  <section class="card card--front" aria-label="Business card front">
    <svg class="pattern-area pattern-area--front-top" viewBox="0 0 280 290" role="img" aria-label="Decorative pattern of interlocking teal rings in the top right corner">
      <defs>
        <linearGradient id="ringsTop" x1="1" y1="0" x2="0" y2="1">
          <stop offset="0" stop-color="#1ba9c4" stop-opacity="0.55"/>
          <stop offset="1" stop-color="#1ba9c4" stop-opacity="0.12"/>
        </linearGradient>
      </defs>
      <path d="M0 0 H280 V290 H210 V180 H105 V80 H0 Z" fill="url(#ringsTop)"/>
    </svg>

    <svg class="pattern-area pattern-area--front-bottom" viewBox="0 0 280 290" role="img" aria-label="Decorative pattern of interlocking teal rings in the bottom left corner">
      <defs>
        <linearGradient id="ringsBottom" x1="0" y1="1" x2="1" y2="0">
          <stop offset="0" stop-color="#1ba9c4" stop-opacity="0.55"/>
          <stop offset="1" stop-color="#1ba9c4" stop-opacity="0.12"/>
        </linearGradient>
      </defs>
      <path d="M0 0 H72 V100 H175 V215 H280 V290 H0 Z" fill="url(#ringsBottom)"/>
    </svg>

    <h1 class="brand-name">Orlan Vitality</h1>
  </section>

  <section class="card card--back" aria-label="Business card back">
    <h2 class="brand-name">Orlan Vitality</h2>

    <p class="person">
      <span class="person-name">Dario Montalbe</span><br>
      <span class="person-role">Wellness Coach, Consultant &amp; Trainer</span>
    </p>

    <ul class="contacts">
      <li class="contact">
        <svg class="contact-icon" viewBox="0 0 32 32" aria-hidden="true">
          <circle cx="16" cy="16" r="16" fill="#ffffff"/>
          <path d="M11 8.5c1-.6 1.8-.2 2.3.7l1.3 2.4c.4.8.2 1.5-.5 2l-1 .7c.8 2 2.3 3.6 4.2 4.6l.8-.9c.6-.7 1.3-.8 2-.3l2.3 1.5c.8.5 1 1.4.4 2.3l-1 1.3c-.9 1.1-2.6 1.2-4.3.4-3.5-1.7-6.3-4.8-7.7-8.3-.7-1.8-.5-3.4.6-4.2z" fill="none" stroke="#1b3c4e" stroke-width="1.5"/>
        </svg>
        <span class="contact-text">Spain: (+34) 612 480 597</span>
      </li>
      <li class="contact">
        <svg class="contact-icon" viewBox="0 0 32 32" aria-hidden="true">
          <circle cx="16" cy="16" r="16" fill="#ffffff"/>
          <path d="M11 8.5c1-.6 1.8-.2 2.3.7l1.3 2.4c.4.8.2 1.5-.5 2l-1 .7c.8 2 2.3 3.6 4.2 4.6l.8-.9c.6-.7 1.3-.8 2-.3l2.3 1.5c.8.5 1 1.4.4 2.3l-1 1.3c-.9 1.1-2.6 1.2-4.3.4-3.5-1.7-6.3-4.8-7.7-8.3-.7-1.8-.5-3.4.6-4.2z" fill="none" stroke="#1b3c4e" stroke-width="1.5"/>
        </svg>
        <span class="contact-text">USA: +1 (555) 318 0264</span>
      </li>
      <li class="contact">
        <svg class="contact-icon" viewBox="0 0 32 32" aria-hidden="true">
          <circle cx="16" cy="16" r="16" fill="#ffffff"/>
          <circle cx="16" cy="16" r="9" fill="none" stroke="#1b3c4e" stroke-width="1.5"/>
          <ellipse cx="16" cy="16" rx="4" ry="9" fill="none" stroke="#1b3c4e" stroke-width="1.2"/>
          <path d="M7 16h18M8.5 11.5h15M8.5 20.5h15" stroke="#1b3c4e" stroke-width="1.2"/>
        </svg>
        <span class="contact-text">www.orlanvitality-example.com</span>
      </li>
    </ul>

    <svg class="pattern-area pattern-area--back-bottom" viewBox="0 0 280 290" role="img" aria-label="Decorative pattern of interlocking teal rings in the bottom right corner">
      <defs>
        <linearGradient id="ringsBack" x1="1" y1="1" x2="0" y2="0">
          <stop offset="0" stop-color="#1ba9c4" stop-opacity="0.55"/>
          <stop offset="1" stop-color="#1ba9c4" stop-opacity="0.12"/>
        </linearGradient>
      </defs>
      <path d="M210 0 H280 V290 H0 V210 H105 V105 H210 Z" fill="url(#ringsBack)"/>
    </svg>
  </section>

</body>
</html>
```